Webdesign for large cottage directory

We have developed a first version of a website that can accommodate large groups (10 to 300 people). The site is English and is aimed at a wide audience ranging from a group of students to a family or a family. For the visitors the site is free and it is the propietaires who pay to see their accommodation. The site is online with just a few fake lodgings and a simple design to the elements that must be appraised (nothing to keep the current design). Our website is here: lodgevista.com (login / pass = admin / 123) Home page (lodgevista.com): on this page section) and lodging by theme (third section). These three points should be highlighted as possible. The displayed map may be slightly modified. Only the background and the color changes when hovering over the mouse. It can be enlarged / retreciated. Below these 3 sections we have some fairly published articles, the latest blog posts and the footer. The menu will be visible throughout the site. Category page (https://lodgevista.fr/gite-departement/aveyron OR https://lodgevista.fr/gites-couchages-121): On these pages we always return the same format with the googlemap, an image 1 text. Below the list of the cottages concerned and the filter options. Product page: The pages presenting the cottages can be of two types: - Either the cottage has no owner and there is no contact for the visitor to the owner that he can retrieve his cottage by registering: example of a page of this type: https://lodgevista.fr/domaine-de-fressanac - The cottage to a propietaire and we are on the classic card. : // lodgevista. en / domain-of-fressanac2 For all products on the site we have nav tab. It's just for testing. We do not want to be in the design for real website. All information must be in the page without login / register page: classic, it's here: https://lodgevista.it/login and https://lodgevista.fr/register Blog homepage (https://lodgevista.fr/blog ): Classic blog page Blog post (https://lodgevista.fr/blog/urltemporaire1551521154) and static page (https://lodgevista.fr/blog/Systeme-classement-lodgevistafr): Nothing special Menu: Menu is an important part of the website. It's the way to navigate on the wbesite.
Faible participation designers
Number of Pages Required
4 page
Colors
Designer to choose colors to be used in the design.
Look and feel
Each slider illustrates characteristics of the customer's brand and the style your logo design should communicate.

```html
<!DOCTYPE html>
<html lang="fr">
<head>
<meta charset="utf-8">
<title>lodgevista.fr — Gîtes de groupe</title>
<link href="https://fonts.googleapis.com/css2?family=Bebas+Neue&family=Open+Sans:wght@400;600;700&display=swap" rel="stylesheet">
<style>
:root{
  --ink:#111111;
  --text:#333333;
  --muted:#555555;
  --white:#ffffff;
  --brand:#1a12f0;
  --brand-line:#5a3cf5;
  --footer:#262626;
  --footer-text:#cfcfcf;
  --display:"Bebas Neue", Impact, sans-serif;
  --body:"Open Sans", Arial, sans-serif;
}
*{box-sizing:border-box;margin:0;padding:0}
html,body{width:1200px;height:4500px;overflow:hidden}
body{position:relative;background:var(--white);font-family:var(--body);color:var(--text)}
.abs{position:absolute}
.photo{position:absolute;display:block}

/* header */
.site-header{left:0;top:0;width:1200px;height:84px;background:var(--white)}
.logo{position:absolute;left:144px;top:18px;font-family:var(--display);font-size:34px;line-height:1;color:var(--brand);letter-spacing:1px}
.main-nav{position:absolute;right:30px;top:34px;display:flex;gap:42px;font-size:13px;font-weight:600;color:var(--ink);text-transform:uppercase}

/* hero */
.hero-title{left:140px;top:470px;font-family:var(--display);font-size:96px;line-height:1;color:var(--white);letter-spacing:1px}
.hero-band{left:120px;top:558px;width:670px;height:72px;background:var(--white)}
.hero-sub{left:144px;top:568px;font-family:var(--display);font-size:52px;line-height:1;color:var(--ink)}

/* search */
.search{left:144px;top:675px;width:912px;height:96px;background:var(--ink);border-bottom:9px solid var(--brand-line);display:flex;align-items:center;padding:0 30px;gap:14px}
.search-field{width:170px;height:38px;background:var(--white);font-size:12px;padding:11px 10px;color:var(--text)}
.search-btn{width:150px;height:40px;background:var(--brand);color:var(--white);font-size:14px;font-weight:700;text-align:center;line-height:40px;margin-left:auto}

/* headings */
.section-title{left:0;width:1200px;text-align:center;font-family:var(--display);color:var(--ink);line-height:1}

/* activities */
.activity{top:1755px;width:240px;height:480px}
.activity-name{position:absolute;left:24px;top:375px;font-family:var(--display);font-size:42px;color:var(--white)}
.activity-text{position:absolute;left:24px;top:420px;width:200px;font-size:12px;line-height:1.45;color:var(--white)}

/* hotels */
.hotel{width:282px;text-align:center}
.hotel-img{width:282px;height:192px}
.hotel-name{margin-top:30px;font-size:13px;font-weight:700;color:var(--ink)}
.hotel-text{margin-top:12px;font-size:12px;line-height:1.5;color:var(--muted)}
.btn-outline{width:141px;height:42px;border:2px solid var(--brand);color:var(--brand);font-family:var(--display);font-size:20px;text-align:center;line-height:40px;left:537px}

/* winter */
.winter-title{left:660px;top:3140px;font-family:var(--display);font-size:112px;line-height:.9;color:var(--white);letter-spacing:3px}
.winter-text{left:672px;top:3330px;width:360px;font-size:12px;line-height:1.5;color:var(--white)}
.btn-solid{left:672px;top:3405px;width:141px;height:42px;background:var(--brand);color:var(--white);font-size:14px;font-weight:700;text-align:center;line-height:42px}

/* blog */
.post{top:3680px;width:282px}
.post-label{font-family:var(--display);font-size:52px;line-height:1;color:var(--ink)}
.post-img{width:282px;height:190px;margin-top:10px}
.post-title{margin-top:30px;font-size:14px;font-weight:700;color:var(--ink)}
.post-text{margin-top:12px;font-size:12px;line-height:1.5;color:var(--muted)}

/* footer */
.site-footer{left:0;top:4245px;width:1200px;height:255px;background:var(--footer);color:var(--footer-text)}
.footer-logo{position:absolute;left:144px;top:30px;font-family:var(--display);font-size:34px;color:var(--brand-line)}
.contact{position:absolute;left:144px;top:84px;font-size:12px;line-height:36px}
.contact li{list-style:none;display:flex;align-items:center;gap:12px}
.footer-nav{position:absolute;top:80px;list-style:none;font-size:11px;font-weight:700;line-height:24px;color:var(--white);text-transform:uppercase}
.social-label{position:absolute;left:900px;top:78px;font-size:12px;color:var(--white)}
.social{position:absolute;left:903px;top:106px;display:flex;gap:10px}
.social span{width:28px;height:28px;border:2px solid var(--white)}
.copyright{position:absolute;left:0;top:220px;width:1200px;text-align:center;font-size:11px}
</style>
</head>
<body>

<header class="site-header abs">
  <div class="logo">lodgevista.fr</div>
  <nav class="main-nav"><span>Home</span><span>About us</span><span>Hosparkirs</span><span>Portfolio</span><span>Blog</span><span>Contact</span></nav>
</header>

<!-- hero -->
<div class="photo" style="left:0;top:84px;width:790px;height:546px;background:linear-gradient(180deg,#0c1c3e 0%,#1f6f78 35%,#3a3040 60%,#b0581d 85%,#2a1810 100%)" role="img" aria-label="Lakeside resort pavilion at dusk under a glowing sky"></div>
<div class="photo" style="left:790px;top:84px;width:410px;height:276px;background:linear-gradient(180deg,#6f9a55 0%,#8fb0b8 45%,#3f9fc8 70%,#d9d2c4 100%)" role="img" aria-label="Outdoor pool with white sun loungers"></div>
<div class="photo" style="left:790px;top:360px;width:410px;height:270px;background:linear-gradient(160deg,#6b4a2e 0%,#caa57a 45%,#efe8de 75%,#8a6a4a 100%)" role="img" aria-label="Bright hotel bedroom with twin beds"></div>
<div class="hero-title abs">Departement.</div>
<div class="hero-band abs"></div>
<div class="hero-sub abs">Gîtes par capacités</div>

<form class="search abs">
  <div class="search-field">1-20</div>
  <div class="search-field">1-20</div>
  <div class="search-field">1-20</div>
  <div class="search-field">1-20</div>
  <div class="search-btn">BOOK NOW</div>
</form>

<div class="photo" style="left:144px;top:837px;width:912px;height:774px;background:radial-gradient(ellipse at 48% 48%,#a9cf7c 0%,#9cc46e 45%,#e9e2cf 70%,#a8d6ee 100%)" role="img" aria-label="Map of France showing numbered départements and main cities"></div>

<h2 class="section-title abs" style="top:1668px;font-size:66px">Notre site</h2>

<div class="activity photo" style="left:0;background:linear-gradient(180deg,#c9d7e6 0%,#7f9bbd 50%,#4e6b93 100%)" role="img" aria-label="Skier on a snowy slope">
  <div class="activity-name">Skiing</div><div class="activity-text">We fill the space content. High-quality, beautiful, solid and</div></div>
<div class="activity photo" style="left:240px;background:linear-gradient(180deg,#5a8fc9 0%,#b9cde0 45%,#c35d2a 70%,#2f3d55 100%)" role="img" aria-label="Two snowboarders in the mountains">
  <div class="activity-name">Boarding</div><div class="activity-text">We fill the space content. High-quality, beautiful, solid and</div></div>
<div class="activity photo" style="left:480px;background:linear-gradient(180deg,#7fa9cf 0%,#6d8656 45%,#4d4a40 75%,#3a3a36 100%)" role="img" aria-label="Cyclists on a mountain road">
  <div class="activity-name">Cycling</div><div class="activity-text">We fill the space content. High-quality, beautiful, solid and</div></div>
<div class="activity photo" style="left:720px;background:linear-gradient(180deg,#8ea1ad 0%,#7b8563 45%,#5f5a44 75%,#3f3d30 100%)" role="img" aria-label="Hikers walking on a mountain trail">
  <div class="activity-name">Hiking</div><div class="activity-text">We fill the space content. High-quality, beautiful, solid and</div></div>
<div class="activity photo" style="left:960px;background:linear-gradient(180deg,#c9b08e 0%,#8c6f55 40%,#9a3a34 65%,#3c3330 100%)" role="img" aria-label="Trekker with a large backpack at sunset">
  <div class="activity-name">Trekking</div><div class="activity-text">We fill the space content. High-quality, beautiful, solid and</div></div>

<h2 class="section-title abs" style="top:2262px;font-size:44px;letter-spacing:1px">Award winning hotels</h2>

<div class="hotel abs" style="left:150px;top:2331px"><div class="hotel-img" style="background:linear-gradient(180deg,#2d2a25,#8a6a48 60%,#c9b497)" role="img" aria-label="Terrace lounge in the middle of downtown"></div><div class="hotel-name">Middle of downtown</div><div class="hotel-text">We fill the space content. High-quality, beautiful, solid and pleasant to the touch.</div></div>
<div class="hotel abs" style="left:465px;top:2331px"><div class="hotel-img" style="background:linear-gradient(180deg,#1e1a22,#7a3a1c 55%,#e08a2a)" role="img" aria-label="Restaurant terrace lit at night"></div><div class="hotel-name">Great Environment</div><div class="hotel-text">We fill the space content. High-quality, beautiful, solid and pleasant to the touch.</div></div>
<div class="hotel abs" style="left:780px;top:2331px"><div class="hotel-img" style="background:linear-gradient(180deg,#6f8a6a,#3fa3b8 55%,#cfc6b2)" role="img" aria-label="Pool beside a garden for breakfast"></div><div class="hotel-name">Free Breakfast</div><div class="hotel-text">We fill the space content. High-quality, beautiful, solid and pleasant to the touch.</div></div>
<div class="hotel abs" style="left:150px;top:2643px"><div class="hotel-img" style="background:linear-gradient(180deg,#4a3a2e,#a88a6a 55%,#e8ddd0)" role="img" aria-label="Freshly made hotel bedroom"></div><div class="hotel-name">We Clean Everyday</div><div class="hotel-text">We fill the space content. High-quality, beautiful, solid and pleasant to the touch.</div></div>
<div class="hotel abs" style="left:465px;top:2643px"><div class="hotel-img" style="background:linear-gradient(180deg,#3a2a1e,#b08a5a 50%,#f2efe8)" role="img" aria-label="Cosy bedroom with warm lighting"></div><div class="hotel-name">Enjoy nightlife</div><div class="hotel-text">We fill the space content. High-quality, beautiful, solid and pleasant to the touch.</div></div>
<div class="hotel abs" style="left:780px;top:2643px"><div class="hotel-img" style="background:linear-gradient(180deg,#5a4634,#8a6a4e 50%,#3a2c22)" role="img" aria-label="Hotel lounge with armchairs"></div><div class="hotel-name">Meet New People</div><div class="hotel-text">We fill the space content. High-quality, beautiful, solid and pleasant to the touch.</div></div>

<div class="btn-outline abs" style="top:2952px">More</div>

<div class="photo" style="left:0;top:3069px;width:1200px;height:441px;background:linear-gradient(180deg,#35507a 0%,#6d86a8 35%,#8a6a4e 55%,#e6ecf2 75%,#f7f9fb 100%)" role="img" aria-label="Snow-covered wooden chalets in the mountains"></div>
<div class="winter-title abs">Winter<br>Weather</div>
<p class="winter-text abs">We fill the space content. High-quality, beautiful and pleasant to the touch. Furniture and decoration of cottages for you.</p>
<div class="btn-solid abs">MORE</div>

<h2 class="section-title abs" style="top:3588px;font-size:84px;letter-spacing:2px">Derniers articles du blog</h2>

<article class="post abs" style="left:144px"><div class="post-label">Post blog 1</div><div class="post-img" style="background:linear-gradient(180deg,#8fb4d6,#c9a77a 45%,#2c8aa8 75%,#1d6a86)" role="img" aria-label="Canal city with gondolas"></div><div class="post-title">Sedail eiusmod tempor</div><div class="post-text">Lorem ipsum dolor sit amet, consectetur adipisci elit, sed eiusmod tempor incidunt</div></article>
<article class="post abs" style="left:459px"><div class="post-label">Post blog 1</div><div class="post-img" style="background:linear-gradient(180deg,#c0507a,#e78aa6 35%,#b88a5a 65%,#5a7a3a)" role="img" aria-label="Garden pergola covered with flowers"></div><div class="post-title">Sedail eiusmod tempor</div><div class="post-text">Lorem ipsum dolor sit amet, consectetur adipisci elit, sed eiusmod tempor incidunt</div></article>
<article class="post abs" style="left:774px"><div class="post-label">Post blog 1</div><div class="post-img" style="background:linear-gradient(180deg,#bcd6ea,#eae4d8 45%,#6fb8cf 75%,#6a8a4a)" role="img" aria-label="Modern villa with a swimming pool"></div><div class="post-title">Sedail eiusmod tempor</div><div class="post-text">Lorem ipsum dolor sit amet, consectetur adipisci elit, sed eiusmod tempor incidunt</div></article>

<div class="btn-outline abs" style="top:4140px">More</div>

<footer class="site-footer abs">
  <div class="footer-logo">lodgevista.fr</div>
  <ul class="contact">
    <li><svg width="12" height="14" viewBox="0 0 12 14"><path d="M6 0a5 5 0 0 0-5 5c0 4 5 9 5 9s5-5 5-9a5 5 0 0 0-5-5zm0 7a2 2 0 1 1 0-4 2 2 0 0 1 0 4z" fill="#fff"/></svg>45 Rue des Lilas, Lyon 69002</li>
    <li><svg width="12" height="12" viewBox="0 0 12 12"><path d="M2 0l2.5 2.5-1.3 1.8a7 7 0 0 0 4.5 4.5l1.8-1.3L12 10l-1.5 2C5 12 0 7 0 1.5z" fill="#fff"/></svg>+33 4 72 00 18 40</li>
    <li><svg width="13" height="10" viewBox="0 0 13 10"><rect width="13" height="10" fill="#fff"/><path d="M0 0l6.5 5L13 0" stroke="#262626" fill="none"/></svg>hello@lodgevista.fr</li>
  </ul>
  <ul class="footer-nav" style="left:480px"><li>Home</li><li>About</li><li>Rooms</li></ul>
  <ul class="footer-nav" style="left:585px"><li>Portfolio</li><li>Blog</li><li>Partnership</li></ul>
  <ul class="footer-nav" style="left:687px"><li>Contact</li></ul>
  <div class="social-label">We are in social networks</div>
  <div class="social"><span></span><span></span><span></span><span></span></div>
  <div class="copyright">Copyright 2019. lodgevista.fr All Right Reserved</div>
</footer>

</body>
</html>
```